BrivoPeak Business Card Design Project

We are looking for a modern, clean business card design for our new company. We are a consulting firm focused on the financial services market providing management and IT consulting to banks, insurance companies, etc. Please include our company logo and company contact information from the attached file in the design. Two versions of the logo are attached, either version is acceptable. Logos are available in other file formats if needed. We would like to include the contact information for both our UK and US offices as well as the following information for each individual card holder: Name, position/title, address, phone number and e-mail address.
Updates
Project Deadline Extended
Reason: A last minute trip over seas has prevented us from finalizing the decision. A decision will be made this week. We apologize for the inconvenience.
Industry/Entity Type
Business
Contact Information for Business Card
Company logo.
Company locations and phone numbers for both the US and UK offices.
Company URL.
Cardholder Name
Cardholder Position/title
Cardholder Address
Cardholder Phone Number
Cardholder e-mail Address
Look and feel
Each slider illustrates characteristics of the customer's brand and the style your logo design should communicate.

```html
<!DOCTYPE html>
<html lang="en">
<head>
<meta charset="utf-8">
<title>BrivoPeak Partners – Business Card</title>
<link rel="stylesheet" href="https://fonts.googleapis.com/css2?family=Open+Sans:wght@400;600;700&display=swap">
<style>
  :root {
    --bg: #e6e6e4;
    --card: #ffffff;
    --navy: #14295a;
    --grey: #4a4a4a;
    --rule: #6e6e6e;
    --shadow: rgba(0,0,0,0.18);
  }
  * { margin: 0; padding: 0; box-sizing: border-box; }
  html, body { width: 1200px; height: 1000px; overflow: hidden; }
  body {
    background: var(--bg);
    font-family: "Open Sans", Arial, sans-serif;
    color: var(--grey);
    position: relative;
  }
  .card {
    position: absolute;
    left: 265px;
    width: 665px;
    height: 397px;
    background: var(--card);
    box-shadow: 0 4px 12px var(--shadow);
  }
  .card--front { top: 73px; }
  .card--back { top: 533px; }

  .brand-name {
    position: absolute;
    color: var(--navy);
    font-weight: 700;
    line-height: 1.05;
    white-space: nowrap;
  }
  .card--front .brand-name { left: 33px; top: 42px; font-size: 38px; }
  .card--back .brand-name {
    left: 0; right: 0; top: 150px;
    text-align: center; font-size: 54px;
  }
  .brand-name small { display: block; font-size: 0.5em; letter-spacing: 0.22em; }

  .holder { position: absolute; left: 33px; top: 175px; }
  .holder-name { color: var(--navy); font-size: 24px; font-weight: 400; line-height: 1.2; }
  .holder-title { font-size: 15px; margin-top: 2px; }

  .divider {
    position: absolute; left: 32px; top: 251px;
    width: 602px; height: 1.5px; background: var(--rule);
  }
  .column {
    position: absolute; top: 251px; height: 114px;
    padding-top: 10px; font-size: 15.5px; line-height: 1.3;
  }
  .column--us { left: 31px; width: 172px; border-right: 1.5px solid var(--rule); }
  .column--uk { left: 225px; width: 169px; border-right: 1.5px solid var(--rule); }
  .column--contact { left: 412px; width: 230px; }
  .office-name { color: var(--navy); font-size: 16px; margin-bottom: 6px; }
  .column--uk .office-name { font-size: 15px; }
  .line { display: flex; align-items: center; gap: 7px; }
  .office-phone { margin-top: 6px; }
  .line svg { width: 14px; height: 14px; fill: var(--navy); flex: none; }
  .column--contact .line { margin-bottom: 2px; }

  .site {
    position: absolute; left: 0; right: 0; top: 348px;
    text-align: center; font-size: 15px; color: var(--grey);
  }
  .site b { color: var(--navy); font-weight: 400; }
</style>
</head>
<body>

<section class="card card--front" aria-label="Business card front">
  <div class="brand-name">BrivoPeak<small>PARTNERS</small></div>

  <div class="holder">
    <p class="holder-name">Dana L. Whitford</p>
    <p class="holder-title">Office Manager</p>
  </div>

  <div class="divider"></div>

  <div class="column column--us">
    <p class="office-name">United States</p>
    <p>418 N Harlow Ave,<br>Suite 204-210<br>Fairview UT 84629</p>
    <p class="line office-phone">
      <svg viewBox="0 0 16 16"><path d="M1 6c0-2 3-3 7-3s7 1 7 3v1h-4V5.5H5V7H1z"/><path d="M3 8h10l1 6H2z"/></svg>
      (801) 555-0147
    </p>
  </div>

  <div class="column column--uk">
    <p class="office-name">Great Britain</p>
    <p>14-16 Marlow Street<br>London<br>E2 9QT</p>
    <p class="line office-phone">
      <svg viewBox="0 0 16 16"><path d="M1 6c0-2 3-3 7-3s7 1 7 3v1h-4V5.5H5V7H1z"/><path d="M3 8h10l1 6H2z"/></svg>
      +44 7700 900412
    </p>
  </div>

  <div class="column column--contact">
    <p class="line">
      <svg viewBox="0 0 16 16"><path d="M4 1h8v14H4zM5.5 3v6h5V3z"/></svg>
      + 000 000 0000
    </p>
    <p class="line">
      <svg viewBox="0 0 16 16"><path d="M1 3h14v1L8 9 1 4z"/><path d="M1 5.5l7 5 7-5V13H1z"/></svg>
      info@brivopeakpartners.com
    </p>
    <p class="line">
      <svg viewBox="0 0 16 16"><circle cx="8" cy="8" r="6.5" fill="none" stroke="#14295a" stroke-width="1.6"/><path d="M2 8h12M8 1.5c-3 3-3 10 0 13M8 1.5c3 3 3 10 0 13" fill="none" stroke="#14295a" stroke-width="1.2"/></svg>
      www.brivopeakpartners.com
    </p>
  </div>
</section>

<section class="card card--back" aria-label="Business card back">
  <div class="brand-name">BrivoPeak<small>PARTNERS</small></div>
  <p class="site">www.<b>brivopeakpartners</b>.com</p>
</section>

</body>
</html>
```